Stationery Design Project

I want to create a single page award for our top sales reps.

I want it to look like a diploma - but with a new school (modern) look and feel, not like a classic diploma.

Corlane is the top Home automation and Solar provider in North America, and our sales team of 2700 reps is amongst the best in the world. This award will recognize our sales reps for "Outstanding Achievment in Professional Sales"

Link to Website:
http://www.corlane-example.ca

The copy will be as follows:

Logo: corlane
This Award Certifies That:
"Lena Dubrow" has demonstrated "Outstanding Achievment in Professional Sales by closing:

"60 Funded Accounts"

Red Deer Alberta 2012

Sales Manager: Peter Halvik
_________________________

Sales Manger: Owen Tracey
_________________________

VP of Sales, Canada: Grant Ellisworth
__________________________

Industry/Entity Type

School

Requirements
Must have
• Corlane Logo

```html
<!DOCTYPE html>
<html lang="en">
<head>
<meta charset="utf-8">
<title>Corlane Sales Award</title>
<link rel="stylesheet" href="https://fonts.googleapis.com/css2?family=Open+Sans:wght@300;400;600;700;800&display=swap">
<style>
  :root {
    --brand-orange: #ff7f00;
    --brand-green: #80ff00;
    --brand-cyan: #33f0e6;
    --ink: #111111;
    --ink-soft: #6a6a6a;
    --title-grey: #b3b3b3;
    --paper: #ffffff;
  }
  html, body {
    margin: 0;
    padding: 0;
    width: 1200px;
    height: 905px;
    overflow: hidden;
    background: var(--paper);
  }
  .award {
    position: relative;
    width: 1200px;
    height: 905px;
    font-family: "Open Sans", Arial, sans-serif;
    color: var(--ink);
    overflow: hidden;
  }
  .side-bar {
    position: absolute;
    left: 0; top: 0;
    width: 83px; height: 905px;
    background: var(--brand-orange);
  }
  .brand-name {
    position: absolute;
    left: 100px; top: 68px;
    margin: 0;
    font-size: 34px;
    font-weight: 600;
    line-height: 1;
    color: var(--ink);
  }
  .header-band {
    position: absolute;
    left: 258px; top: 78px;
    width: 942px; height: 26px;
    background: var(--brand-orange);
  }
  .centered {
    position: absolute;
    left: 0;
    width: 1190px;
    margin: 0;
    text-align: center;
    white-space: nowrap;
  }
  .award-title {
    top: 158px;
    font-size: 88px;
    font-weight: 300;
    line-height: 1;
    color: var(--title-grey);
  }
  .certifies {
    position: absolute;
    left: 386px; top: 328px;
    margin: 0;
    font-size: 15px;
    font-weight: 400;
    color: var(--ink-soft);
    letter-spacing: -0.2px;
  }
  .recipient {
    position: absolute;
    left: 384px; top: 335px;
    margin: 0;
    font-size: 70px;
    font-weight: 300;
    line-height: 1.15;
    letter-spacing: -1px;
    color: var(--ink);
  }
  .demonstrated {
    top: 474px;
    font-size: 21px;
    color: var(--ink-soft);
  }
  .achievement {
    top: 551px;
    font-size: 20.4px;
    font-weight: 700;
    color: var(--ink);
  }
  .accounts {
    top: 592px;
    font-weight: 800;
    color: var(--brand-orange);
    line-height: 1;
  }
  .accounts-count { font-size: 38px; }
  .accounts-label { font-size: 25.5px; }
  .signatories {
    position: absolute;
    left: 115px; top: 741px;
    margin: 0; padding: 0;
    list-style: none;
    font-size: 14px;
    color: var(--ink-soft);
  }
  .signatories li { height: 55px; }
  .site-link {
    position: absolute;
    right: 144px; top: 846px;
    white-space: nowrap;
    text-align: right;
    font-size: 15px;
    font-weight: 700;
    color: var(--ink-soft);
  }
  .colour-chips {
    position: absolute;
    left: 1067px; top: 841px;
  }
</style>
</head>
<body>
<main class="award">
  <div class="side-bar"></div>
  <p class="brand-name">Corlane</p>
  <div class="header-band"></div>

  <h1 class="centered award-title">AWARD</h1>

  <p class="certifies">THIS AWARD CERTIFIES THAT:</p>
  <p class="recipient">Lena Dubrow</p>

  <p class="centered demonstrated">HAS DEMONSTRATED</p>
  <p class="centered achievement">"Outstanding Achievment in Professional Sales by closing:</p>
  <p class="centered accounts"><span class="accounts-count">60</span> <span class="accounts-label">FUNDED ACCOUNTS</span></p>

  <ul class="signatories">
    <li>Sales Manager: Peter Halvik</li>
    <li>Sales Manger: Owen Tracey</li>
    <li>VP of Sales, Canada: Grant Ellisworth</li>
  </ul>

  <div class="site-link">www.corlane-example.ca</div>
  <svg class="colour-chips" width="96" height="30" viewBox="0 0 96 30" aria-hidden="true">
    <rect x="0" y="0" width="30" height="30" fill="var(--brand-orange)"/>
    <rect x="33" y="0" width="30" height="30" fill="var(--brand-green)"/>
    <rect x="66" y="0" width="30" height="30" fill="var(--brand-cyan)"/>
  </svg>
</main>
</body>
</html>
```